Website Layout for PlateNova

PlateNova is a company that will be dedicated (for now) to publishing recipes with the nutrition facts. Run by a nutritionist. In the future there may be a mobile app.

We need layout for 3 of the pages of the website. NO PROGRAMMING, only layout and graphic design. Not very complicated.

--Please view the details in the attached document--
We want a layout design for the pages: P.01, P.02 and P.03

Logo is also attached. Please don't hesitate if you want to modify the logo to fit your idea. The design should be clean, visually attractive and refreshing to look at. It should be sleek and a feel of technology, yet also natural and culinary.

Some examples to get ideas:

http://www.amberladlejournal.com/
http://www.tasliwavera.org/site/
http://thevelmorhaus.com/products/mix-slab
Updates

Project Deadline Extended
Reason: I extend the deadline for this week to allow you space for work on the observations made to your design and to provide the P.02 and P.03 designs. We greatly appreciate your hard work and are thrilled with your ideas.

Target Market(s)

Young people that live alone or want to optimize their cooking.
Young, modern housewives with a smartphone.

Industry/Entity Type

Nutrition

Requirements
Must have
• --Please view the details in the attached document--
NO PROGRAMMING. Only layout and graphic design.

```html
<!DOCTYPE html>
<html lang="en">
<head>
<meta charset="utf-8">
<title>PlateNova — Home</title>
<link rel="stylesheet" href="https://fonts.googleapis.com/css2?family=Open+Sans:ital,wght@0,400;0,600;0,700;1,400&family=Amatic+SC:wght@700&display=swap">
<style>
  :root {
    --accent: #e2512c;
    --accent-dark: #c9382a;
    --red: #d0302c;
    --green: #7a9a2a;
    --band: #e8f1e2;
    --footer: #eef4e8;
    --line: #d5dfcd;
    --ink: #1f1f1f;
    --muted: #6b6b6b;
    --white: #ffffff;
  }
  * { box-sizing: border-box; margin: 0; padding: 0; }
  html, body { width: 1134px; height: 1200px; overflow: hidden; }
  body {
    position: relative;
    font-family: "Open Sans", sans-serif;
    color: var(--ink);
    background: radial-gradient(ellipse 520px 420px at 820px 300px, #fbf3e8 0%, rgba(255,255,255,0) 70%),
                radial-gradient(ellipse 360px 320px at 120px 560px, #fcefee 0%, rgba(255,255,255,0) 70%),
                var(--white);
  }
  .top-rule { position: absolute; left: 0; top: 0; width: 1134px; height: 3px; background: var(--accent); }

  .site-header { position: absolute; left: 0; top: 3px; width: 1134px; height: 71px; background: rgba(255,255,255,.9); }
  .brand { position: absolute; left: 177px; top: 18px; display: flex; align-items: center; gap: 8px; }
  .brand-mark { width: 36px; height: 36px; background: var(--accent); border-radius: 4px; }
  .brand-name { font-size: 20px; font-weight: 600; color: #3a3a3a; }

  .main-nav { position: absolute; top: 28px; font-size: 14.5px; }
  .main-nav a { position: absolute; white-space: nowrap; color: var(--ink); text-decoration: none; }
  .main-nav a.active { color: var(--red); }

  .menu-toggle { position: absolute; left: 784px; top: 26px; width: 27px; height: 27px; background: #444; display: flex; flex-direction: column; justify-content: center; align-items: center; gap: 2px; }
  .menu-toggle span { width: 13px; height: 2px; background: var(--white); }
  .btn { position: absolute; top: 26px; height: 27px; font-size: 12px; font-weight: 600; display: flex; align-items: center; justify-content: center; }
  .btn-login { left: 818px; width: 67px; border: 1px solid #cfcfcf; color: #777; background: var(--white); }
  .btn-join { left: 889px; width: 67px; background: var(--accent); border: 1px solid var(--accent-dark); color: var(--white); }

  .tool-band { position: absolute; left: 0; top: 74px; width: 1134px; height: 40px; background: var(--band); border-top: 1px solid var(--line); border-bottom: 1px solid var(--line); }
  .collapse-btn { position: absolute; left: 177px; top: 7px; width: 27px; height: 23px; border: 2px solid #444; border-radius: 2px; background: var(--white); }
  .collapse-btn::after { content: ""; position: absolute; left: 7px; top: 8px; width: 9px; height: 3px; background: #333; }
  .search { position: absolute; left: 787px; top: 6px; width: 170px; height: 25px; background: var(--white); border: 1px solid #cfcfcf; font-size: 12px; color: #888; padding: 4px 10px; }
  .search svg { position: absolute; right: 8px; top: 6px; }

  .intro { position: absolute; left: 212px; top: 156px; width: 710px; text-align: center; font-size: 13.6px; line-height: 17.5px; }
  .learn-more { position: absolute; left: 0; top: 224px; width: 1134px; display: flex; justify-content: center; align-items: center; gap: 6px; font-size: 10px; color: var(--green); letter-spacing: .3px; }
  .learn-more .tick { width: 24px; height: 24px; border: 2px solid var(--green); border-radius: 50%; display: flex; align-items: center; justify-content: center; }

  .card { position: absolute; width: 189px; overflow: hidden; color: var(--white); }
  .card .photo { position: absolute; inset: 0; }
  .card .caption { position: absolute; left: 0; right: 0; bottom: 0; padding: 0 12px 6px 18px; background: linear-gradient(rgba(70,60,50,.35), rgba(50,40,35,.55)); }
  .card h2 { font-family: "Amatic SC", cursive; font-size: 28px; font-weight: 700; line-height: 26px; letter-spacing: .5px; padding-top: 6px; }
  .card p { font-size: 10px; line-height: 12px; }
  .card .facts { font-size: 7.5px; font-style: italic; margin-top: 12px; padding-top: 6px; border-top: 1px solid rgba(255,255,255,.15); margin-left: -2px; }

  .card-featured .caption { top: 193px; background: #2f2f2f; padding-top: 8px; }
  .card-featured h2, .card-featured .facts { color: var(--red); }
  .card-featured .facts { position: absolute; bottom: 8px; left: 20px; right: 0; border-top: 1px solid #444; padding-top: 8px; }
  .bite-it { position: absolute; left: 11px; top: 8px; display: flex; gap: 2px; z-index: 2; }
  .bite-it .label { width: 66px; height: 25px; background: var(--red); font-size: 11.5px; font-weight: 600; display: flex; align-items: center; justify-content: center; }
  .bite-it .like { width: 26px; height: 25px; background: var(--white); display: flex; align-items: center; justify-content: center; }

  .site-footer { position: absolute; left: 0; top: 986px; width: 1134px; height: 214px; background: var(--footer); border-top: 1px solid var(--line); text-align: center; font-size: 12px; }
  .social { position: absolute; left: 527px; top: 55px; display: flex; gap: 2px; }
  .social span { width: 24px; height: 24px; border-radius: 50%; border: 2px solid; }
  .social .s1 { border-color: var(--red); }
  .social .s2 { border-color: var(--green); }
  .social .s3 { border-color: #e8a236; }
  .footer-links { position: absolute; left: 0; top: 88px; width: 1134px; line-height: 20px; }
</style>
</head>
<body>
  <div class="top-rule"></div>

  <header class="site-header">
    <div class="brand"><span class="brand-mark"></span><span class="brand-name">PlateNova</span></div>
    <nav class="main-nav">
      <a class="active" style="left:546px">Home</a>
      <a style="left:605px">About Us</a>
      <a style="left:684px">Contact Us</a>
    </nav>
    <div class="menu-toggle"><span></span><span></span><span></span></div>
    <div class="btn btn-login">Login</div>
    <div class="btn btn-join">Join Us</div>
  </header>

  <div class="tool-band">
    <div class="collapse-btn"></div>
    <div class="search">Search
      <svg width="11" height="11" viewBox="0 0 11 11"><circle cx="4.5" cy="4.5" r="3.3" fill="none" stroke="#888" stroke-width="1.6"/><line x1="7" y1="7" x2="10" y2="10" stroke="#888" stroke-width="1.8"/></svg>
    </div>
  </div>

  <p class="intro">Welcome to introduction text lorem ipsum dolor sit amet, consectetur adipisicing elit, sed do eiusmod tempor incididunt ut labore et dolore magna aliqua. Ut enim ad minim veniam, quis nostrud exercitation ullamco laboris nisi ut aliquip commodo consequat.</p>

  <div class="learn-more">LEARN
    <span class="tick"><svg width="12" height="10" viewBox="0 0 12 10"><path d="M1 5 L4.5 8.5 L11 1.5" fill="none" stroke="#7a9a2a" stroke-width="2.4"/></svg></span>
    MORE</div>

  <!-- column 1 -->
  <article class="card card-featured" style="left:177px;top:293px;height:289px">
    <div class="photo" role="img" aria-label="Layered sandwich squares with jam filling" style="bottom:96px;background:linear-gradient(160deg,#6b8a3a 0%,#e9dcc0 35%,#f2e4c4 60%,#d9a24a 100%)"></div>
    <div class="bite-it"><span class="label">Bites It</span><span class="like"><svg width="16" height="16" viewBox="0 0 16 16"><path d="M2 7h3v7H2zM6 7l3-5c1 0 2 1 1.5 2.5L10 6h4c1 0 1.5 1 1 2l-1.5 5c-.3.7-.8 1-1.5 1H6z" fill="none" stroke="#444" stroke-width="1.2"/></svg></span></div>
    <div class="caption">
      <h2>Breakfast</h2>
      <p>Lorem ipsum dolor sit amet consectetur</p>
      <div class="facts">Calories &nbsp;1XX0 &nbsp; - &nbsp; Fat Time 1XX</div>
    </div>
  </article>
  <article class="card" style="left:177px;top:590px;height:296px">
    <div class="photo" role="img" aria-label="Bacon and cheese burger on salad leaves" style="background:linear-gradient(170deg,#5f8a2c 0%,#3f6a1f 30%,#9a3b1c 60%,#e2a21a 78%,#5a2a18 100%)"></div>
    <div class="caption">
      <h2>Category 5</h2>
      <p>Lorem ipsum dolor sit amet consectetur</p>
      <div class="facts">Calories &nbsp;1XX0 &nbsp; - &nbsp; Fat Time 1XX</div>
    </div>
  </article>

  <!-- column 2 -->
  <article class="card" style="left:374px;top:293px;height:353px">
    <div class="photo" role="img" aria-label="Baked quinoa and spinach bites on a white plate" style="background:linear-gradient(160deg,#8a6a3a 0%,#c9b58a 30%,#e8e4dc 55%,#b9a274 80%,#6e5a36 100%)"></div>
    <div class="caption">
      <h2>Pastry</h2>
      <p>Lorem ipsum dolor sit amet consectetur</p>
      <div class="facts">Calories &nbsp;1XX0 &nbsp; - &nbsp; Fat Time 1XX</div>
    </div>
  </article>
  <article class="card" style="left:374px;top:654px;height:225px">
    <div class="photo" role="img" aria-label="Nut-coated cheese balls with a fork" style="background:linear-gradient(160deg,#7a7570 0%,#b7a58a 35%,#d9c9a6 60%,#9c8c74 100%)"></div>
    <div class="caption">
      <h2>Category 6</h2>
      <p>Lorem ipsum dolor sit amet consectetur</p>
      <div class="facts">Calories &nbsp;1XX0 &nbsp; - &nbsp; Fat Time 1XX</div>
    </div>
  </article>

  <!-- column 3 -->
  <article class="card" style="left:571px;top:293px;height:304px">
    <div class="photo" role="img" aria-label="Seeded crispbread scored into pieces" style="background:linear-gradient(150deg,#6a5a48 0%,#8b7760 35%,#4a3e33 60%,#7d6b56 100%)"></div>
    <div class="caption">
      <h2>Soups</h2>
      <p>Lorem ipsum dolor sit amet consectetur</p>
      <div class="facts">Calories &nbsp;1XX0 &nbsp; - &nbsp; Fat Time 1XX</div>
    </div>
  </article>
  <article class="card" style="left:571px;top:604px;height:304px">
    <div class="photo" role="img" aria-label="Puff pastries filled with berry jam" style="background:linear-gradient(160deg,#e8c48a 0%,#9a2a3a 30%,#f0d7a8 55%,#a8203a 75%,#e6c79a 100%)"></div>
    <div class="caption">
      <h2>Category 7</h2>
      <p>Lorem ipsum dolor sit amet consectetur</p>
      <div class="facts">Calories &nbsp;1XX0 &nbsp; - &nbsp; Fat Time 1XX</div>
    </div>
  </article>

  <!-- column 4 -->
  <article class="card" style="left:769px;top:293px;height:225px">
    <div class="photo" role="img" aria-label="Lentil sloppy joe bun with avocado on a blue plate" style="background:linear-gradient(160deg,#6a4a2a 0%,#c08a4e 30%,#6a9aa0 55%,#5a3a22 80%,#8aa8a8 100%)"></div>
    <div class="caption">
      <h2>Category 4</h2>
      <p>Lorem ipsum dolor sit amet consectetur</p>
      <div class="facts">Calories &nbsp;1XX0 &nbsp; - &nbsp; Fat Time 1XX</div>
    </div>
  </article>
  <article class="card" style="left:769px;top:526px;height:268px">
    <div class="photo" role="img" aria-label="Mini pizza muffins with basil and tomato dip" style="background:linear-gradient(160deg,#9cb2c0 0%,#e8dcc0 30%,#e6c27a 55%,#8a5a36 80%,#4a4a48 100%)"></div>
    <div class="caption">
      <h2>Category 8</h2>
      <p>Lorem ipsum dolor sit amet consectetur</p>
      <div class="facts">Calories &nbsp;1XX0 &nbsp; - &nbsp; Fat Time 1XX</div>
    </div>
  </article>

  <footer class="site-footer">
    <div class="social"><span class="s1"></span><span class="s2"></span><span class="s3"></span></div>
    <div class="footer-links">-----<br>Terms and Policy<br>©<br>2014</div>
  </footer>
</body>
</html>
```